Skin care manufacturer looking for packaging design for new skin care brand.

We need a design and logo for a skin care brand to be sold at retail stores and online in the United States and Europe. The design will be for 1.7oz - 2oz serums that will not have a retail box. The name of the brand is Orvia Lune and should be a luxurious brand that is approachable. The brand will consist of 4 GLOW serums - Vitamin C, Collagen, Retinol and Hyaluronic Acid that all contain Dead Sea Minerals. Images shown are for inspiration only. Color of bottles can be varied based on design and bottles can be screen printed or labeled.

```html
<!DOCTYPE html>
<html lang="en">
<head>
<meta charset="utf-8">
<title>Orvia Lune – 4 Glow Serums</title>
<link href="https://fonts.googleapis.com/css2?family=Jost:wght@300;400&display=swap" rel="stylesheet">
<style>
  :root {
    --bg: #f2f2f2;
    --cap: #1e1e1f;
    --cap-rib: #2c2c2d;
    --ink-light: rgba(255,255,255,0.92);
    --ink-soft: rgba(255,255,255,0.8);
    --band: rgba(255,255,255,0.86);
    --onyx: #323234;
    --onyx-deep: #262628;
    --lime: #88a93c;
    --lime-deep: #4f6a1e;
    --rose: #d63a6e;
    --rose-deep: #8c1d43;
  }
  * { margin: 0; padding: 0; box-sizing: border-box; }
  html, body { width: 1200px; height: 1010px; overflow: hidden; background: var(--bg); }
  body { position: relative; font-family: "Jost", sans-serif; font-weight: 300; }

  .serum { position: absolute; top: 190px; width: 210px; height: 644px; }
  .serum--onyx { left: 171px; --tone: var(--onyx); --tone-deep: var(--onyx-deep); }
  .serum--lime { left: 500px; --tone: var(--lime); --tone-deep: var(--lime-deep); }
  .serum--rose { left: 825px; --tone: var(--rose); --tone-deep: var(--rose-deep); }

  .serum__overcap {
    position: absolute; left: 28px; top: 0; width: 154px; height: 116px;
    border: 2px solid #d4d4d4; border-bottom: none; border-radius: 6px 6px 0 0;
    background: rgba(255,255,255,0.35);
  }
  .serum__pump {
    position: absolute; left: 58px; top: 28px; width: 86px; height: 90px;
    background: #3a3a3b; border-radius: 4px 4px 0 0;
  }
  .serum__collar {
    position: absolute; left: 26px; top: 116px; width: 158px; height: 103px;
    border-radius: 5px;
    background: repeating-linear-gradient(90deg, var(--cap) 0 5px, var(--cap-rib) 5px 8px);
  }
  .serum__body {
    position: absolute; left: 0; top: 219px; width: 210px; height: 425px;
    background: var(--tone);
    border-radius: 70px 70px 16px 16px / 60px 60px 12px 12px;
    text-align: center; color: var(--ink-light);
  }
  .serum__brand {
    position: absolute; top: 60px; left: 0; right: 0;
    font-size: 26px; font-weight: 300; letter-spacing: 0.06em;
    color: var(--ink-light);
  }
  .serum__band {
    position: absolute; top: 137px; left: 0; right: 0; height: 47px;
    background: var(--band);
  }
  .serum__title {
    display: block; line-height: 47px; font-size: 42px; font-weight: 300;
    color: var(--tone-deep); letter-spacing: 0.01em;
  }
  .serum__range {
    position: absolute; top: 187px; left: 0; right: 0;
    font-size: 23px; line-height: 30px; letter-spacing: 0.02em;
  }
  .serum__ingredients {
    position: absolute; top: 235px; left: 0; right: 0;
    font-size: 15px; line-height: 18px; color: var(--ink-soft); letter-spacing: 0.01em;
  }
  .serum__minerals {
    position: absolute; top: 276px; left: 24px; right: 24px; height: 20px;
    background: var(--band); color: var(--tone-deep);
    font-size: 12.5px; line-height: 20px; font-weight: 400;
  }
  .serum__size {
    position: absolute; top: 343px; left: 0; right: 0;
    font-size: 12px; color: var(--ink-soft); letter-spacing: 0.03em;
  }
</style>
</head>
<body>
  <div class="serum serum--onyx">
    <div class="serum__overcap"></div>
    <div class="serum__pump"></div>
    <div class="serum__collar"></div>
    <div class="serum__body">
      <p class="serum__brand">Orvia Lune</p>
      <div class="serum__band"><span class="serum__title">4 GLOW</span></div>
      <p class="serum__range">SERUMS</p>
      <p class="serum__ingredients">VITAMIN C • COLLAGEN<br>RETINOL • HYALURONIC ACID</p>
      <p class="serum__minerals">All Contain Dead Sea Minerals</p>
      <p class="serum__size">1.7OZ - 2OZ</p>
    </div>
  </div>

  <div class="serum serum--lime">
    <div class="serum__overcap"></div>
    <div class="serum__pump"></div>
    <div class="serum__collar"></div>
    <div class="serum__body">
      <p class="serum__brand">Orvia Lune</p>
      <div class="serum__band"><span class="serum__title">4 GLOW</span></div>
      <p class="serum__range">SERUMS</p>
      <p class="serum__ingredients">VITAMIN C • COLLAGEN<br>RETINOL • HYALURONIC ACID</p>
      <p class="serum__minerals">All Contain Dead Sea Minerals</p>
      <p class="serum__size">1.7OZ - 2OZ</p>
    </div>
  </div>

  <div class="serum serum--rose">
    <div class="serum__overcap"></div>
    <div class="serum__pump"></div>
    <div class="serum__collar"></div>
    <div class="serum__body">
      <p class="serum__brand">Orvia Lune</p>
      <div class="serum__band"><span class="serum__title">4 GLOW</span></div>
      <p class="serum__range">SERUMS</p>
      <p class="serum__ingredients">VITAMIN C • COLLAGEN<br>RETINOL • HYALURONIC ACID</p>
      <p class="serum__minerals">All Contain Dead Sea Minerals</p>
      <p class="serum__size">1.7OZ - 2OZ</p>
    </div>
  </div>
</body>
</html>
```